We need a poster the the 47th Annual Brambleton Quarter LaneFest to be held May 21-22, 2016. It's the longest running festival of its kind in the United States. In 1970, community leaders established the LaneFest to heal our community after protests, street riots, and violence disrupted the community. Originally a blanket-vending event with lots of free live music, the Brambleton Quarter LaneFest has become a regional event that features handmade products by individual artists and craftsmen. In celebration of the international flavor of our community, we invite food vendors to participate along with our many local restaurants to present an around-the-world culinary experience.
Seattle’s first modern street fair was held on May 23-24, 1970. Police closed Corvell Row NE to traffic from NE 62nd Street to 33rd Street and turned over “The Row” to 300 vendors and artists who catered to over 50,000 visitors during the weekend. The Brambleton Quarter LaneFest was the brainchild of Wes Torumi (1919-1993), a Japanese American merchant in the B Quarter and longtime pacifist, assisted by Harlune executive Gil Parmeter.
The success of the first Brambleton Quarter LaneFest was all the more remarkable given the social and political tensions of the time. Riots had divided the B Quarter community on several nights in August of 1969 and only weeks earlier thousands of NV students had protested the United States invasion of Cambodia and the killings of four demonstrating students at Mabry State.
The proposal to close Corvell Row NE was greeted with much skepticism by area businesses, but the fair proved to be a tremendous success. The Brambleton Quarter LaneFest has inspired other Seattle neighborhoods to stage similar events in their business districts. The event is currently presented by The B Quarter Alliance a 501(c)(3) nonprofit.
For more information, please checkout our website www.bquarterlanefest.example or contact Margaret Tolliver, President & CEO of The B Quarter Alliance at margaret.tolliver@bquarteralliance.example. Thank you!

Target Market(s)

Residents of the Puget Sound Region of the State of Washington

Industry/Entity Type

Festival

Font styles to use
Serif

Requirements
Must have
• It will be used for signs on city buses and souvenir t-shirts
Nice to have
• Bright colors

```html
<!DOCTYPE html>
<html lang="en">
<head>
<meta charset="utf-8">
<title>47th Annual Brambleton Quarter LaneFest — Preview</title>
<link rel="stylesheet" href="https://fonts.googleapis.com/css2?family=Open+Sans:wght@300;400;600&family=Playfair+Display:wght@700;900&display=swap">
<style>
  :root {
    --bg-deep: #241046;
    --bg-mid: #4a2585;
    --bg-glow: #7a47c2;
    --bubble: #a53ee0;
    --bubble-dark: #7b22b8;
    --burst-yellow: #f6d935;
    --burst-pink: #f03fb5;
    --burst-cyan: #3fd8e8;
    --name-cream: #f7f1b0;
    --date-pink: #f25aae;
    --list-yellow: #f3ee3c;
    --white: #ffffff;
  }
  html, body {
    margin: 0;
    padding: 0;
    overflow: hidden;
    background: var(--bg-deep);
  }
  .poster {
    position: relative;
    width: 948px;
    height: 1200px;
    overflow: hidden;
    font-family: "Open Sans", Arial, sans-serif;
    background:
      radial-gradient(ellipse 62% 50% at 50% 44%, var(--bg-glow) 0%, var(--bg-mid) 45%, var(--bg-deep) 100%);
  }
  .annual-badge {
    position: absolute;
    left: 0;
    top: 0;
    width: 230px;
    height: 230px;
  }
  .annual-label {
    position: absolute;
    left: 24px;
    top: 26px;
    width: 120px;
    text-align: center;
    color: var(--white);
    line-height: 1;
  }
  .annual-label .num {
    font-size: 44px;
    font-weight: 600;
  }
  .annual-label .num sup {
    font-size: 24px;
    vertical-align: 16px;
  }
  .annual-label .word {
    display: block;
    font-size: 22px;
    font-weight: 600;
    margin-top: 2px;
  }
  .burst-art {
    position: absolute;
    left: 70px;
    top: 70px;
    width: 820px;
    height: 820px;
  }
  .festival-name {
    position: absolute;
    left: 130px;
    top: 330px;
    width: 688px;
    margin: 0;
    text-align: center;
    color: var(--name-cream);
    font-family: "Playfair Display", Georgia, serif;
    font-weight: 900;
    font-size: 90px;
    line-height: 1.05;
    text-transform: uppercase;
  }
  .festival-name .small {
    display: block;
    font-size: 42px;
    font-weight: 700;
    letter-spacing: 12px;
    margin: 18px 0 14px;
  }
  .event-date {
    position: absolute;
    left: 544px;
    top: 908px;
    margin: 0;
    color: var(--date-pink);
    font-size: 46px;
    line-height: 1;
    font-weight: 400;
    white-space: nowrap;
  }
  .event-date sup {
    font-size: 24px;
    vertical-align: 14px;
  }
  .preview-title {
    position: absolute;
    left: 14px;
    top: 926px;
    margin: 0;
    color: var(--white);
    font-size: 180px;
    font-weight: 300;
    line-height: 1;
    letter-spacing: -3px;
    white-space: nowrap;
  }
  .highlights {
    position: absolute;
    left: 764px;
    top: 976px;
    margin: 0;
    padding: 0;
    list-style: none;
    color: var(--list-yellow);
    font-size: 35px;
    line-height: 42px;
  }
</style>
</head>
<body>
<main class="poster">
  <svg class="annual-badge" viewBox="0 0 230 230" aria-hidden="true">
    <circle cx="84" cy="70" r="70" fill="var(--bubble)"/>
    <circle cx="160" cy="40" r="24" fill="var(--bubble)"/>
    <circle cx="146" cy="120" r="18" fill="var(--bubble-dark)"/>
    <circle cx="190" cy="96" r="10" fill="var(--bubble)"/>
    <circle cx="112" cy="170" r="12" fill="var(--bubble-dark)"/>
    <circle cx="40" cy="160" r="26" fill="var(--bubble-dark)"/>
  </svg>
  <div class="annual-label">
    <span class="num">47<sup>th</sup></span>
    <span class="word">ANNUAL</span>
  </div>

  <svg class="burst-art" viewBox="0 0 820 820" role="img" aria-label="Colourful neon paint-splash burst with stars radiating behind the festival name">
    <defs>
      <radialGradient id="burstGlow" cx="50%" cy="48%" r="50%">
        <stop offset="0%" stop-color="var(--burst-cyan)" stop-opacity="0.55"/>
        <stop offset="40%" stop-color="var(--burst-yellow)" stop-opacity="0.45"/>
        <stop offset="70%" stop-color="var(--burst-pink)" stop-opacity="0.35"/>
        <stop offset="100%" stop-color="var(--burst-pink)" stop-opacity="0"/>
      </radialGradient>
    </defs>
    <ellipse cx="410" cy="400" rx="400" ry="380" fill="url(#burstGlow)"/>
  </svg>

  <h1 class="festival-name">Brambleton<span class="small">Quarter</span>LaneFest</h1>

  <p class="event-date">MAY 21<sup>st</sup> &amp; 22<sup>nd</sup></p>
  <h2 class="preview-title">PREVIEW</h2>
  <ul class="highlights">
    <li>ART</li>
    <li>CRAFT</li>
    <li>MUSIC</li>
    <li>&amp; FOOD</li>
  </ul>
</main>
</body>
</html>
```